Business card for start up company

SIMPLE, CLEAN, FRESH, MODERN, SOPHISTICATED. professional. experienced, easy to deal with, expert in the field. local ethics.

professional business card for Forge Bay Industries. using company logo supplied and images.

GENERAL ENGINEERING - MACHINING - WELDING - MAINTENANCE

Forge Bay Industries Ltd is a locally owned mechanical engineering company that specialises in general and mechanical engineering, as well as steel fabrication, welding, repairs and maintenance.

We specialise in the design, welding, fabrication and installation of stainless and mild steel fabrications. We service commercial and residential clients; large or small projects; production line or one off designs.

We have built a solid reputation for quality and service for our machinery and engineering work around Northland NZ. For innovative, cost effective and efficient engineering solutions, to suit a wide range of commercial, residential and rural applications.

Target Market(s)

boat builders. DIY. industrial. RESIDENTIAL. COMMERCIAL

Industry/Entity Type

Mechanical Engineering

Contact Information for Business Card

CONTACT / SERVICES SIDE
Forge Bay Industries Ltd.
Design | Machining | Welding | Fabrication | Installation | Maintenance
www.forgebayindustries.example.nz
kevin@forgebayindustries.example.nz

Font styles to use
Serif

Colors

Designer to choose colors to be used in the design.

Requirements
Must have
• LOGO ONLY WITH NEGATIVE SPACE ON FRONT SIDE
• services and contact side , either use stock photos (supplied) as background or background supplied in logo photos.
Nice to have
• use the symbol icon in logo on contact/ services side, , enlarged, transparent and faded into the background with text over the top on the
• Design | Machining | Welding | Fabrication | Installation | Maintenance
• the above services to be subtle, along the bottom edge of the services side. can i also have another proof with eh above services featuring on the bottom edge of the LOGO FRONT side to see if the text looks better with or without.
Should not have
• crowded, busy, different fonts. different casing.
• use fonts in the logo files designer to make font decision.

```html
<!DOCTYPE html>
<html lang="en">
<head>
<meta charset="utf-8">
<title>Forge Bay Industries – Business Card</title>
<link rel="stylesheet" href="https://fonts.googleapis.com/css2?family=Exo+2:wght@300;400;600&display=swap">
<style>
  :root{
    --bg:#e9e6e1;
    --card:#0b0b0b;
    --block:#3a3a3a;
    --block-soft:#2a2a2a;
    --orange:#ec5b24;
    --brown:#3a2a22;
    --white:#ffffff;
    --grey:#b9b9b9;
    --icon:#d9d9d9;
  }
  *{margin:0;padding:0;box-sizing:border-box}
  html,body{width:1200px;height:804px;overflow:hidden;background:var(--bg)}
  body{font-family:"Exo 2",sans-serif;position:relative}
  .card{position:absolute;top:242px;width:560px;height:320px;background:var(--card);overflow:hidden;box-shadow:0 10px 30px rgba(0,0,0,.25)}
  .card--services{left:25px}
  .card--contact{left:615px}

  /* services side */
  .symbol-area{position:absolute;left:150px;top:30px;width:300px;height:260px;
    background:linear-gradient(135deg,var(--block) 0%,var(--block-soft) 100%);opacity:.85}
  .accent{position:absolute;background:var(--orange)}
  .accent--top{left:0;top:30px;width:16px;height:70px}
  .accent--end{right:0;top:40px;width:16px;height:70px}
  .chip{position:absolute;right:70px;top:190px;width:34px;height:34px;background:var(--brown)}
  .company-name{position:absolute;left:40px;top:42px;font-size:30px;font-weight:600;color:var(--white);letter-spacing:.5px;text-transform:uppercase}
  .services{position:absolute;left:40px;top:96px;font-size:15px;font-weight:300;color:var(--white);line-height:1.5}

  /* contact side */
  .brand{position:absolute;left:28px;top:26px;display:flex;align-items:center;gap:12px}
  .brand__square{width:28px;height:28px;background:var(--white)}
  .brand__name{font-size:22px;font-weight:400;color:var(--white);letter-spacing:.5px;text-transform:uppercase}
  .row{position:absolute;left:60px;right:0;display:flex;align-items:center;gap:10px}
  .row__icon{flex:none;background:var(--icon);display:flex;align-items:center;justify-content:center}
  .row__band{flex:1;background:var(--orange);color:var(--white);display:flex;align-items:center;padding-left:14px}
  .row--name{top:110px}
  .row--name .row__icon{width:40px;height:40px}
  .row--name .row__band{height:52px;font-size:24px;font-weight:600;text-transform:uppercase;letter-spacing:.5px}
  .job-title{font-weight:300;font-size:17px;margin-left:10px}
  .row--email{top:190px}
  .row--web{top:232px}
  .row--email .row__icon,.row--web .row__icon{width:26px;height:26px}
  .row--email .row__band,.row--web .row__band{height:30px;font-size:15px;font-weight:400}
  .row--web .row__icon{visibility:hidden}
</style>
</head>
<body>
  <section class="card card--services">
    <div class="symbol-area" role="img" aria-label="Enlarged faded company symbol in dark grey"></div>
    <div class="accent accent--top"></div>
    <div class="accent accent--end"></div>
    <div class="chip"></div>
    <h1 class="company-name">Forge Bay Industries</h1>
    <p class="services">Design | Machining | Welding | Fabrication<br>| Installation | Maintenance</p>
  </section>

  <section class="card card--contact">
    <div class="brand">
      <span class="brand__square"></span>
      <span class="brand__name">Forge Bay Industries</span>
    </div>
    <div class="row row--name">
      <span class="row__icon">
        <svg width="22" height="22" viewBox="0 0 22 22" aria-hidden="true"><circle cx="11" cy="7" r="5" fill="#ec5b24"/><path d="M2 21c0-5 4-8 9-8s9 3 9 8z" fill="#ec5b24"/></svg>
      </span>
      <span class="row__band">Mara Quinlan <span class="job-title">| Job Title</span></span>
    </div>
    <div class="row row--email">
      <span class="row__icon">
        <svg width="16" height="12" viewBox="0 0 16 12" aria-hidden="true"><rect x="0.5" y="0.5" width="15" height="11" fill="none" stroke="#ec5b24"/><path d="M1 1l7 6 7-6" fill="none" stroke="#ec5b24"/></svg>
      </span>
      <span class="row__band">kevin@forgebayindustries.example.nz</span>
    </div>
    <div class="row row--web">
      <span class="row__icon"></span>
      <span class="row__band">www.forgebayindustries.example.nz</span>
    </div>
  </section>
</body>
</html>
```